Information One Page for Email

I am looking for a informative attachment I can send with an introductive email for Ridgeview Cable Works. Something I can also Mail.

Ridgeview Cable Works is the leader in Rebar Post Tension Cable Placement and Post Tension Cable repair. Outside of cable placement and repair we do concrete repair, Parking Garage restoration and

Content

Post Tension Repair and Concrete Restoration
Post-tensioning is a revolutionary method in concrete construction that enhances the strength and durability of structures. However, like all construction ele-ments, post-tension cables can experience wear and damage over time. Ensuring timely and effective repair is crucial for maintaining the safety and integrity of your building.
Why Post-Tension Cable Repair is Essential
1. **Structural Integrity**: Damaged or deteriorated cables can compromise the structural integrity of your building, leading to safety hazards and potential structural failures.
2. **Extended Lifespan**: Regular maintenance and repair of post-tension cables extend the lifespan of your structure, ensuring it remains safe and function-al for years to come.
3. **Cost-Effective**: Addressing cable issues early on prevents more severe damage and costly repairs down the line.
Common Signs of Post-Tension Cable Issues
- Cracks in concrete surfaces
- Unusual noises or popping sounds
- Visible cable ends or broken strands
- Water leakage through cracks
Our Repair Process
1. **Inspection and Assessment**: Our team conducts a thorough inspection to identify the extent of the damage and determine the appropriate repair meth-ods.
2. **Cable Repair or Replacement**: Depending on the severity, we either re-pair the existing cables or replace them with new ones to restore full functional-ity.
3. **Sealing and Protection**: After repairing, we seal the affected areas to protect against moisture and future damage.
4. **Quality Assurance**: We perform rigorous quality checks to ensure the repairs meet industry standards and the structure is safe for use.
Why Choose Us
- **Expertise and Experience**: With years of experience in post-tension cable repair, our team is skilled in handling even the most complex repairs efficiently and effectively.
- **Advanced Technology**: We use the latest technology and materials to ensure durable and long-lasting repairs.
- **Customer Satisfaction**: Our commitment to quality and customer satisfaction sets us apart. We work closely with our clients to ensure their needs are met and expectations exceeded.
Contact Us
If you suspect issues with your post-tension cables or need a routine inspection, don't hesitate to contact us. Our experts are ready to provide the best solutions to keep your structures safe and secure.
Ensure the safety and longevity of your building with our professional post-tension cable repair services. Trust us to deliver quality and reliability every time.

```html
<!DOCTYPE html>
<html lang="en">
<head>
<meta charset="utf-8">
<title>Ridgeview Cable Works – Post Tension Repair</title>
<link href="https://fonts.googleapis.com/css2?family=Poppins:wght@400;500;600;700;800&display=swap" rel="stylesheet">
<style>
:root{
  --green:#1b7a48;
  --green-deep:#176b3f;
  --ink:#232323;
  --grey-box:#6b6b6b;
  --panel:#efefef;
  --page:#ffffff;
  --backdrop:#e4e4e4;
  --text:#2b2b2b;
}
*{margin:0;padding:0;box-sizing:border-box}
html,body{width:897px;height:1200px;overflow:hidden}
body{background:var(--backdrop);font-family:'Poppins',sans-serif;color:var(--text)}
.sheet{position:absolute;left:30px;top:0;width:836px;height:1200px;background:var(--page);overflow:hidden}
.abs{position:absolute}

.brand-strip{background:var(--green);top:0;height:110px;width:15px}
.brand-box{left:48px;top:0;width:410px;height:110px;background:var(--page);display:flex;align-items:center;justify-content:center}
.brand-name{font-weight:600;color:var(--green);font-size:24px;line-height:1.15;text-align:left}

.hero-band{left:0;top:110px;width:483px;height:333px;background:var(--green)}
.hero-bracket{left:0;top:0}
.headline{left:69px;top:143px;font-weight:800;font-size:41px;line-height:41px;letter-spacing:-0.5px}
.headline .light{color:#fff}
.headline .dark{color:var(--ink)}
.intro{left:33px;top:333px;width:440px;height:110px;background:var(--ink);color:#fff;font-size:10.2px;line-height:13.2px;padding:20px 20px 0 37px}

.dark-block{left:668px;top:0;width:168px;height:459px;background:var(--ink)}
.frame-line{left:485px;top:43px;width:326px;height:400px;border:1.5px solid #fff}
.photo{background:linear-gradient(180deg,#b9b6ae,#8d8a82 60%,#7a7466)}
.photo-main{left:492px;top:63px;width:299px;height:355px;border:4px solid #fff}
.photo-a{left:496px;top:423px;width:133px;height:92px;background:linear-gradient(180deg,#cdd8e2,#9aa3a6 55%,#5d6063)}
.photo-b{left:645px;top:423px;width:132px;height:92px;background:linear-gradient(180deg,#8a8676,#5b5a52)}
.tick-bar{left:697px;top:430px;width:4px;height:14px;background:var(--green)}

.benefit-icon{width:34px;height:34px}
.benefit-title{left:111px;font-weight:600;font-size:20px;color:var(--green);line-height:24px}
.benefit-text{left:111px;width:300px;font-size:11px;line-height:13.3px}

.signs{left:65px;top:738px;width:325px;height:160px;background:var(--grey-box);color:#fff;padding:10px 0 0 23px}
.signs h2{font-weight:600;font-size:20px;line-height:25px;margin-bottom:10px}
.signs li{list-style:none;font-size:11.5px;line-height:19px;display:flex;align-items:center;gap:5px}

.process{left:418px;top:532px;width:354px;height:378px;background:var(--panel)}
.process h2{position:absolute;left:25px;top:10px;font-weight:600;font-size:21px;color:var(--green)}
.step{left:26px;width:318px;height:63px;border:1.3px solid var(--green);padding:3px 0 0 41px}
.step h3{font-weight:700;font-size:13.4px;line-height:16px;color:var(--green)}
.step p{font-size:10.4px;line-height:12.4px;padding-right:6px}
.step-icon{left:14px;width:29px;height:29px}

.choose-head{left:65px;top:910px;width:707px;height:33px;background:var(--ink);color:#fff;font-weight:600;font-size:20px;text-align:center;line-height:33px}
.choose-cols{left:65px;top:943px;width:707px;height:116px;display:flex}
.choose-col{flex:1;background:var(--green);color:#fff;text-align:center;padding:11px 14px 0}
.choose-col.mid{background:var(--green-deep)}
.choose-col h3{font-weight:600;font-size:15.5px;line-height:20px;margin-bottom:4px}
.choose-col p{font-size:10.6px;line-height:13.2px}

.closing{left:60px;top:1072px;width:716px;text-align:center;font-size:11px;line-height:13.3px}
.contact{top:1130px;height:28px;display:flex;align-items:center;gap:6px}
.phone{left:77px;font-weight:600;font-size:18px;color:var(--ink)}
.web{left:276px;font-weight:600;font-size:13.6px;color:var(--ink)}
.social{left:592px;font-weight:600;font-size:13.4px;letter-spacing:2px;color:var(--ink)}
.divider{top:1130px;width:1px;height:28px;background:#cfcfcf}
.dot{width:18px;height:18px;border-radius:50%;background:var(--green);display:inline-block}
</style>
</head>
<body>
<div class="sheet">

  <div class="abs brand-strip" style="left:33px"></div>
  <div class="abs brand-strip" style="left:458px"></div>
  <div class="abs brand-box"><div class="brand-name">Ridgeview<br>Cable Works</div></div>

  <div class="abs dark-block"></div>
  <div class="abs hero-band"></div>
  <svg class="abs hero-bracket" width="483" height="350" viewBox="0 0 483 350">
    <polyline points="62,146 48,146 48,316 233,316 233,336" fill="none" stroke="#fff" stroke-width="1.3"/>
    <polygon points="227,334 239,334 233,341" fill="#fff"/>
  </svg>
  <h1 class="abs headline">
    <span class="light">POST TENSION</span><br>
    <span class="light">REPAIR &amp;</span><br>
    <span class="dark">CONCRETE</span><br>
    <span class="dark">RESTORATION</span>
  </h1>
  <p class="abs intro">Post-tensioning is a revolutionary method in concrete construction ,that enhances the strength and durability of structures. However like all construction ele-ments post-tension cables can experience wear and damage over time. Ensuring timely and effective repair is crucial for maintaining the safety and integrity of your building. Why Post-Tension Cable Repair is Essential</p>

  <div class="abs frame-line"></div>
  <div class="abs photo photo-main" role="img" aria-label="Photo of a multi-storey concrete building facade under repair with a worker on a balcony"></div>
  <div class="abs photo-a" role="img" aria-label="Photo of a construction site with a crane and post-tension cable layout"></div>
  <div class="abs tick-bar"></div>
  <div class="abs photo-b" role="img" aria-label="Photo of a post-tension cable grid laid on a slab before pouring"></div>

  <!-- benefits -->
  <svg class="abs benefit-icon" style="left:66px;top:489px" viewBox="0 0 34 34"><rect x="3" y="3" width="31" height="31" fill="none" stroke="#555" stroke-width="1"/><rect x="0" y="0" width="31" height="31" fill="var(--green)"/><path d="M8 22h15M9 17l6-7 6 7M9 12h13M10 22l5-5 5 5" stroke="#fff" stroke-width="1.3" fill="none"/></svg>
  <h2 class="abs benefit-title" style="top:480px">Structural Integrity</h2>
  <p class="abs benefit-text" style="top:508px">Damaged or deteriorated cables can compromise the structural integrity of your building, leading to safety hazards and potential structural failures.</p>

  <svg class="abs benefit-icon" style="left:66px;top:566px" viewBox="0 0 34 34"><rect x="3" y="3" width="31" height="31" fill="none" stroke="#555" stroke-width="1"/><rect x="0" y="0" width="31" height="31" fill="var(--green)"/><rect x="10" y="8" width="11" height="14" fill="none" stroke="#fff" stroke-width="1.3"/><circle cx="17" cy="20" r="4" fill="var(--green)" stroke="#fff" stroke-width="1.3"/></svg>
  <h2 class="abs benefit-title" style="top:565px">Extended Lifespan</h2>
  <p class="abs benefit-text" style="top:594px">Regular maintenance and repair of post-tension cables extend the lifespan of your structure, ensuring it remains safe and function-al for years to come.</p>

  <svg class="abs benefit-icon" style="left:66px;top:660px" viewBox="0 0 34 34"><rect x="3" y="3" width="31" height="31" fill="none" stroke="#555" stroke-width="1"/><rect x="0" y="0" width="31" height="31" fill="var(--green)"/><path d="M7 24v-4M11 24v-7M15 24v-10" stroke="#fff" stroke-width="2"/><circle cx="21" cy="18" r="5" fill="none" stroke="#fff" stroke-width="1.3"/><path d="M9 13l6-6 3 3" stroke="#fff" stroke-width="1.3" fill="none"/></svg>
  <h2 class="abs benefit-title" style="top:656px">Cost-Effective</h2>
  <p class="abs benefit-text" style="top:684px;left:113px">Addressing cable issues early on prevents more severe damage and costly repairs down the line.</p>

  <section class="abs signs">
    <h2>Common Signs of<br>Post-Tension Cable Issues</h2>
    <ul>
      <li><svg width="9" height="9" viewBox="0 0 10 10"><circle cx="5" cy="5" r="4" fill="none" stroke="#fff"/><path d="M3 5l1.5 1.5L7 3.5" stroke="#fff" fill="none"/></svg>Cracks in concrete surfaces</li>
      <li><svg width="9" height="9" viewBox="0 0 10 10"><circle cx="5" cy="5" r="4" fill="none" stroke="#fff"/><path d="M3 5l1.5 1.5L7 3.5" stroke="#fff" fill="none"/></svg>Unusual noises or popping sounds</li>
      <li><svg width="9" height="9" viewBox="0 0 10 10"><circle cx="5" cy="5" r="4" fill="none" stroke="#fff"/><path d="M3 5l1.5 1.5L7 3.5" stroke="#fff" fill="none"/></svg>Visible cable ends or broken strands</li>
      <li><svg width="9" height="9" viewBox="0 0 10 10"><circle cx="5" cy="5" r="4" fill="none" stroke="#fff"/><path d="M3 5l1.5 1.5L7 3.5" stroke="#fff" fill="none"/></svg>Water leakage through cracks</li>
    </ul>
  </section>

  <section class="abs process">
    <h2>Our Repair Process</h2>
    <div class="abs step" style="top:53px"><h3>INSPECTION AND ASSESSMENT</h3><p>Our team conducts a thorough inspection to identify the extent of the damage and determine the appropriate repair meth-ods.</p></div>
    <svg class="abs step-icon" style="top:65px" viewBox="0 0 29 29"><rect x="3" y="3" width="26" height="26" fill="none" stroke="#555"/><rect width="26" height="26" fill="var(--ink)"/><rect x="7" y="6" width="11" height="14" fill="none" stroke="#fff" stroke-width="1.2"/><circle cx="17" cy="17" r="3.5" fill="var(--ink)" stroke="#fff" stroke-width="1.2"/></svg>

    <div class="abs step" style="top:132px"><h3>CABLE REPAIR OR REPLACEMENT</h3><p>Depending on the severity, we either re-pair the existing cables or replace them with new ones to restore full functional-ity.</p></div>
    <svg class="abs step-icon" style="top:144px" viewBox="0 0 29 29"><rect x="3" y="3" width="26" height="26" fill="none" stroke="#555"/><rect width="26" height="26" fill="var(--ink)"/><path d="M8 20l8-12M12 20l6-10" stroke="#fff" stroke-width="1.4"/></svg>

    <div class="abs step" style="top:212px"><h3>SEALING AND PROTECTION</h3><p>After repairing, we seal the affected areas to protect against moisture and future damage.</p></div>
    <svg class="abs step-icon" style="top:224px" viewBox="0 0 29 29"><rect x="3" y="3" width="26" height="26" fill="none" stroke="#555"/><rect width="26" height="26" fill="var(--ink)"/><circle cx="12" cy="12" r="5" fill="none" stroke="#fff" stroke-width="2.2" stroke-dasharray="2.5 1.5"/><circle cx="18" cy="18" r="3.5" fill="#fff"/></svg>

    <div class="abs step" style="top:294px"><h3>QUALITY ASSURANCE</h3><p>We perform rigorous quality checks to ensure the repairs meet industry standards and the structure is safe for use.</p></div>
    <svg class="abs step-icon" style="top:306px" viewBox="0 0 29 29"><rect x="3" y="3" width="26" height="26" fill="none" stroke="#555"/><rect width="26" height="26" fill="var(--ink)"/><circle cx="13" cy="13" r="7" fill="none" stroke="#fff" stroke-width="1.3"/><path d="M10 13l2 2 4-4" stroke="#fff" stroke-width="1.3" fill="none"/></svg>
  </section>

  <h2 class="abs choose-head">Why Choose Us</h2>
  <div class="abs choose-cols">
    <div class="choose-col"><h3>Expertise and Experience</h3><p>With years of experience in post-tension cable repair, our team is skilled in handling even the most complex repairs efficiently and effectively.</p></div>
    <div class="choose-col mid"><h3>Advanced Technology</h3><p>We use the latest technology and materials to ensure durable and long-lasting repairs.</p></div>
    <div class="choose-col"><h3>Customer Satisfaction</h3><p>Our commitment to quality and customer satisfaction sets us apart. We work closely with our clients to ensure their needs are met and expectations exceeded.</p></div>
  </div>

  <p class="abs closing">If you suspect issues with your post-tension cables or need a routine inspection, don't hesitate to contact us. Our experts are ready to provide the best solutions to keep your structures safe and secure. Ensure the safety and longevity of your building with our professional post-tension cable repair services. Trust us to deliver quality and reliability every time.</p>

  <div class="abs contact phone"><svg width="18" height="18" viewBox="0 0 18 18"><circle cx="9" cy="9" r="9" fill="var(--green)"/><path d="M6 5l2 0 1 2.5-1.2 1a6 6 0 0 0 2.7 2.7l1-1.2 2.5 1v2c-4.5.5-8.5-3.5-8-8z" fill="#fff"/></svg>(555) 014-2290</div>
  <div class="abs divider" style="left:256px"></div>
  <div class="abs contact web"><svg width="18" height="18" viewBox="0 0 18 18"><circle cx="9" cy="9" r="9" fill="var(--green)"/><circle cx="9" cy="9" r="5" fill="none" stroke="#fff" stroke-width="1"/><path d="M4 9h10M9 4v10" stroke="#fff" stroke-width="1"/></svg>www.ridgeviewcableworks.com</div>
  <div class="abs divider" style="left:559px"></div>
  <div class="abs contact social">Follow us on <span class="dot" style="margin-left:6px"></span><span class="dot"></span></div>

</div>
</body>
</html>
```